Redesign of our homepage

We are a company that operates in the Wellness tourism sector. We are starting a project to redesign our homepage. See the screenshots. The main idea is that the banner image and the text on the banner are dynamically replaced depending on whether a user clicks on the "Thumb up" or the "Thumb down" icon.
You can see a live version of our homepage at http://demo.velqorambe.com

Requirements
Must have
• Must abide by style and look & feel of the current site.
It is important to demonstrate the functionality that enables the banner image and text being refreshed at each click of a ThumbUp or ThumbDown icons. In others words the Javascript must work.

Let me add some more context on the project.

Actually the thumb up and thumb down are possible answers to question/comment dynamically displayed at the location of the current text "Experience That Make You tell an unforgettable story".
An example of a comment/question is "I need a program that would help limit my stress levels and make me look great and feel fantastic". Or "I need an activity that will reduce my stress."
So a user would have to click on a thumb up or thumb down to approve or disapprove these questions/comments..
Based on this information, I think you could move the thumbs up to the left and right side of the text (the comment/question) respectively. And move the reset underneath in the middle.

Maybe it's a good idea to reduce the font size of that text as well.

And now to the dropdown list. We need only 2 of them, and not 3 as you have displayed.
One of them contain the list:
-- I need a weekend retreat
-- ! need a week or more retreat
The other would contain a list of countries.
The drop down values must be selected before the thumbs up and down thumbs are active.
Therefore you should move them above the question/comment text.
And finally about the thumbs and reset icons. Please put them in a round orange color and make them a bit bigger.

```html
<!DOCTYPE html>
<html lang="en">
<head>
<meta charset="utf-8">
<title>Velqorambe – Wellness Retreats</title>
<link href="https://fonts.googleapis.com/css2?family=Poppins:wght@300;400;500;600&display=swap" rel="stylesheet">
<style>
:root{
  --orange:#f29a1f;
  --orange-dark:#e0860c;
  --yellow:#fbc02d;
  --text:#333;
  --muted:#666;
  --white:#fff;
  --black:#000;
  --teal:#2cb5a0;
}
*{box-sizing:border-box;margin:0;padding:0}
html,body{width:1200px;height:2989px;overflow:hidden;background:var(--white);font-family:'Poppins',sans-serif;color:var(--text)}
.page{position:relative;width:1200px;height:2989px;overflow:hidden}

/* header */
.site-header{position:absolute;left:0;top:0;width:1200px;height:76px;background:var(--white);border-bottom:2px solid #e3e3e3}
.brand{position:absolute;left:42px;top:18px;display:flex;align-items:center;gap:8px;font-size:30px;font-weight:300;color:var(--orange)}
.brand-dot{width:16px;height:16px;border-radius:50%;background:#666}
.currency{position:absolute;left:279px;top:31px;font-size:15px;font-weight:500;color:var(--orange)}
.nav{position:absolute;top:31px;font-size:16px;color:#444;display:flex;align-items:center;gap:6px}
.btn-auth{position:absolute;top:14px;height:48px;background:var(--yellow);border-radius:5px;color:#333;font-size:15px;display:flex;align-items:center;justify-content:center;gap:10px}

/* hero */
.hero{position:absolute;left:0;top:76px;width:1200px;height:610px;
  background:linear-gradient(180deg,#2f74c9 0%,#6fa6de 28%,#a9cdea 45%,#2cb9c9 62%,#0f8fb3 70%,#cfe6e6 80%,#e9e1d0 100%)}
.hero-wave{position:absolute;left:0;top:570px;width:1200px;height:120px}
.select{position:absolute;top:152px;width:270px;height:52px;background:var(--white);border-radius:5px;font-size:14px;color:#333;display:flex;align-items:center;padding:0 14px;gap:8px;box-shadow:0 2px 6px rgba(0,0,0,.12)}
.select .label{flex:1}
.question{position:absolute;left:330px;top:244px;width:540px;text-align:center;color:var(--white);font-size:26px;font-weight:500;line-height:36px;text-shadow:0 1px 4px rgba(0,0,0,.25)}
.hero-sub{position:absolute;left:0;top:452px;width:1200px;text-align:center;color:var(--white);font-size:19px;font-weight:600}
.action{position:absolute;width:68px;height:68px;border-radius:50%;background:var(--orange);display:flex;align-items:center;justify-content:center;box-shadow:0 3px 8px rgba(0,0,0,.2)}
.action-reset{width:60px;height:60px;background:var(--orange-dark)}

/* sidebar */
.filter{position:absolute;left:169px;width:274px;height:66px;background:var(--white);border-bottom:2px solid #eee;box-shadow:0 1px 4px rgba(0,0,0,.06);display:flex;align-items:center;justify-content:space-between;padding:0 28px 0 20px;font-size:17px;font-weight:600;color:#222}
.package-panel{position:absolute;left:169px;top:937px;width:274px;height:308px;background:var(--white);box-shadow:0 1px 5px rgba(0,0,0,.1);padding:26px 0 0 14px}
.package-panel li{list-style:none;display:flex;align-items:center;gap:8px;font-size:15px;color:#555;height:31.7px}

/* cards */
.card-img{position:absolute;left:520px;width:488px;height:277px}
.card-title{position:absolute;left:525px;width:500px;font-size:32.5px;font-weight:400;line-height:42px;color:#555;letter-spacing:-.1px}
.feature{position:absolute;left:530px;display:flex;align-items:center;gap:20px;font-size:15px;color:#666}
.feature svg{width:20px;height:18px}

/* pagination */
.pager{position:absolute;top:2576px;left:496px;display:flex;gap:6px;font-size:8px}
.pager span{height:20px;border:1px solid #ddd;display:flex;align-items:center;justify-content:center;padding:0 8px;color:#555;background:#fff}
.pager .current{background:var(--orange);color:#fff;border-color:var(--orange)}
.pager .disabled{color:#bbb}

/* footer */
.footer-wave{position:absolute;left:0;top:2660px;width:1200px;height:90px}
.site-footer{position:absolute;left:0;top:2745px;width:1200px;height:244px;background:var(--black);color:var(--white)}
.fcol{position:absolute;top:24px;width:92px;font-size:6.5px;line-height:12px;overflow-wrap:break-word}
.fcol h4{color:var(--teal);font-size:6.5px;font-weight:500;margin-bottom:24px;text-transform:uppercase}
.fcol p{font-weight:500}
.copyright{position:absolute;left:274px;top:187px;font-size:7.5px;font-weight:500}
.connect{position:absolute;left:754px;top:180px;display:flex;align-items:center;gap:3px;font-size:7.5px;font-weight:500}
.social{width:22px;height:22px;border-radius:50%;background:#2e6fc0;border:1.5px solid #fff}
</style>
</head>
<body>
<div class="page">

<header class="site-header">
  <div class="brand"><span>velqorambe</span><span class="brand-dot"></span></div>
  <div class="currency">EUR <svg width="14" height="10" viewBox="0 0 14 10"><path d="M2 2l5 5 5-5" fill="none" stroke="#444" stroke-width="1.6"/></svg></div>
  <div class="nav" style="left:376px">Wellness Retreats <svg width="14" height="10" viewBox="0 0 14 10"><path d="M2 2l5 5 5-5" fill="none" stroke="#444" stroke-width="1.6"/></svg></div>
  <div class="nav" style="left:554px"><svg width="20" height="14" viewBox="0 0 20 14"><path d="M5 12h11a3.5 3.5 0 0 0 0-7 5 5 0 0 0-9.5 1A3 3 0 0 0 5 12z" fill="none" stroke="#555" stroke-width="1.3"/></svg>Our Climate Pledge</div>
  <div class="nav" style="left:767px"><svg width="26" height="16" viewBox="0 0 26 16"><path d="M2 6l6-4 5 3 5-3 6 4-6 7-5-3-5 3z" fill="none" stroke="#555" stroke-width="1.3"/></svg> Partners</div>
  <div class="btn-auth" style="left:928px;width:110px"><svg width="18" height="16" viewBox="0 0 18 16"><path d="M2 2v12M6 8h10M6 8l4-4M6 8l4 4" fill="none" stroke="#222" stroke-width="2"/></svg>Sign In</div>
  <div class="btn-auth" style="left:1048px;width:110px"><svg width="22" height="20" viewBox="0 0 22 20"><circle cx="9" cy="6" r="4" fill="none" stroke="#222" stroke-width="1.6"/><path d="M2 18c0-4 3-6 7-6s5 1 6 2M16 13v6M13 16h6" fill="none" stroke="#222" stroke-width="1.6"/></svg>Sign Up</div>
</header>

<section class="hero" role="img" aria-label="Tropical beach with turquoise sea, blue sky and a red frozen cocktail on the sand"></section>
<svg class="hero-wave" viewBox="0 0 1200 120" preserveAspectRatio="none"><path d="M0 10C80-10 160 30 240 70S380 110 470 60 700 10 850 20 1000 30 1080 20 1160-10 1200 20V120H0z" fill="#fff"/></svg>

<!-- retreat finder: two selects, then the statement with thumbs -->
<div class="select" style="left:320px">
  <svg width="16" height="16" viewBox="0 0 16 16"><rect x="1.5" y="3" width="13" height="11" rx="1" fill="none" stroke="#333" stroke-width="1.3"/><path d="M1.5 6h13M5 1v3M11 1v3" stroke="#333" stroke-width="1.3"/></svg>
  <span class="label">I need a weekend retreat</span>
  <svg width="12" height="8" viewBox="0 0 12 8"><path d="M1 1h10L6 7z" fill="#444"/></svg>
</div>
<div class="select" style="left:610px">
  <svg width="12" height="16" viewBox="0 0 12 16"><path d="M6 15s5-5.5 5-9A5 5 0 0 0 1 6c0 3.5 5 9 5 9z" fill="#333"/><circle cx="6" cy="6" r="2" fill="#fff"/></svg>
  <span class="label">Choose a country</span>
  <svg width="12" height="8" viewBox="0 0 12 8"><path d="M1 1h10L6 7z" fill="#444"/></svg>
</div>

<div class="action" style="left:236px;top:254px" aria-label="Disagree">
  <svg width="32" height="32" viewBox="0 0 26 26"><path d="M4 4h5v11H4zM10 4h9a2 2 0 0 1 2 2l1 7a2 2 0 0 1-2 2h-5l1 5a2 2 0 0 1-3 1l-3-6z" fill="#fff" stroke="#fff" stroke-width="1.5" stroke-linejoin="round"/></svg>
</div>
<p class="question">I need a program that would help limit my stress levels and make me look great and feel fantastic</p>
<div class="action" style="left:896px;top:254px" aria-label="Agree">
  <svg width="32" height="32" viewBox="0 0 26 26"><path d="M4 11h5v11H4zM10 11l3-6a2 2 0 0 1 3 1l-1 5h5a2 2 0 0 1 2 2l-1 7a2 2 0 0 1-2 2h-9z" fill="#fff" stroke="#fff" stroke-width="1.5" stroke-linejoin="round"/></svg>
</div>
<div class="action action-reset" style="left:570px;top:366px" aria-label="Reset">
  <svg width="28" height="28" viewBox="0 0 24 24"><path d="M6 8a8 8 0 1 1-1 7" fill="none" stroke="#fff" stroke-width="2.6"/><path d="M3 3v7h7z" fill="#fff"/></svg>
</div>
<p class="hero-sub">Incorporated With Climate Awareness</p>

<!-- sidebar filters -->
<div class="filter" style="top:733px">DESTINATIONS <svg width="16" height="10" viewBox="0 0 16 10"><path d="M0 1h16L8 9z" fill="#444"/></svg></div>
<div class="filter" style="top:800px">CATEGORIES <svg width="16" height="10" viewBox="0 0 16 10"><path d="M0 1h16L8 9z" fill="#444"/></svg></div>
<div class="filter" style="top:866px">PACKAGE <svg width="16" height="10" viewBox="0 0 16 10"><path d="M0 9h16L8 1z" fill="#444"/></svg></div>
<ul class="package-panel">
  <li><svg width="14" height="14" viewBox="0 0 14 14"><rect x="2" y="3" width="10" height="9" fill="none" stroke="#444" stroke-width="1.3"/><path d="M2 6h10M5 1v3M9 1v3" stroke="#444" stroke-width="1.3"/></svg>3 days / 2 nights</li>
  <li><svg width="14" height="14" viewBox="0 0 14 14"><circle cx="7" cy="4" r="3" fill="#222"/><path d="M1 13c0-4 3-5 6-5s6 1 6 5z" fill="#222"/></svg>Minimum number of persons: 1</li>
  <li><svg width="14" height="14" viewBox="0 0 14 14"><circle cx="7" cy="4" r="3" fill="#222"/><path d="M1 13c0-4 3-5 6-5s6 1 6 5z" fill="#222"/></svg>Maximum group size: 8</li>
  <li><svg width="14" height="14" viewBox="0 0 14 14"><circle cx="7" cy="4" r="3" fill="#222"/><path d="M1 13c0-4 3-5 6-5s6 1 6 5z" fill="#222"/></svg>Minimum age: 10 years</li>
  <li><svg width="14" height="14" viewBox="0 0 14 14"><circle cx="7" cy="7" r="6" fill="#6ec1c0"/></svg>Image 3.02 tCO2(e)</li>
  <li><svg width="14" height="14" viewBox="0 0 14 14"><path d="M7 2c4 0 6 3 5 6H2c-1-3 1-6 5-6zM7 8v5" fill="#8bc34a" stroke="#8bc34a"/></svg>Image 193 trees</li>
</ul>

<!-- cards -->
<div class="card-img" style="top:734px;background:linear-gradient(180deg,#b8b8b2 0%,#a7a9a0 45%,#6f7a45 75%,#4e5a30 100%)" role="img" aria-label="Giraffe and a cheering safari guide on the savanna"></div>
<h2 class="card-title" style="top:1040px">3 Days Big Five Tented Safari, Kruger National Park, South Africa</h2>
<div class="feature" style="top:1199px"><svg viewBox="0 0 20 18"><rect x="1" y="3" width="18" height="13" rx="2" fill="#222"/></svg>Flexible cancellation policyImage</div>
<div class="feature" style="top:1231px"><svg viewBox="0 0 20 18"><path d="M10 1v16M3 9l7-2 7 2M7 16h6" stroke="#222" stroke-width="2.2" fill="none"/></svg>Airport transfer includedImage</div>
<div class="feature" style="top:1263px"><svg viewBox="0 0 20 18"><path d="M2 14a8 8 0 0 1 16 0zM1 16h18" fill="#222" stroke="#222" stroke-width="1.5"/></svg>Meals includedImage</div>

<div class="card-img" style="top:1345px;background:linear-gradient(180deg,#bcbcb6 0%,#8c9a68 35%,#6f8a44 60%,#9a8a70 100%)" role="img" aria-label="Rancher on a chestnut horse beside a calf on open grassland"></div>
<h2 class="card-title" style="top:1650px">2 Days Wild West Ranch<br>Exploration And Bike Holiday In<br>Colorado, USA</h2>
<div class="feature" style="top:1809px"><svg viewBox="0 0 20 18"><rect x="1" y="3" width="18" height="13" rx="2" fill="#222"/></svg>Flexible cancellation policyImage</div>
<div class="feature" style="top:1841px"><svg viewBox="0 0 20 18"><path d="M10 1v16M3 9l7-2 7 2M7 16h6" stroke="#222" stroke-width="2.2" fill="none"/></svg>Airport transfer includedImage</div>
<div class="feature" style="top:1873px"><svg viewBox="0 0 20 18"><path d="M2 14a8 8 0 0 1 16 0zM1 16h18" fill="#222" stroke="#222" stroke-width="1.5"/></svg>Meals includedImage</div>

<div class="card-img" style="top:1960px;background:linear-gradient(180deg,#9dc0d8 0%,#6a9a3c 25%,#5d8a34 55%,#8a7a5e 100%)" role="img" aria-label="Group of riders on horseback along a farm track by a cornfield"></div>
<h2 class="card-title" style="top:2265px">5 Days Full Ranch Experience<br>And Horsemanship Training In<br>Mulla Creek, NSW, Australia</h2>
<div class="feature" style="top:2424px"><svg viewBox="0 0 20 18"><rect x="1" y="3" width="18" height="13" rx="2" fill="#222"/></svg>Flexible cancellation policyImage</div>
<div class="feature" style="top:2456px"><svg viewBox="0 0 20 18"><path d="M10 1v16M3 9l7-2 7 2M7 16h6" stroke="#222" stroke-width="2.2" fill="none"/></svg>Airport transfer includedImage</div>
<div class="feature" style="top:2488px"><svg viewBox="0 0 20 18"><path d="M2 14a8 8 0 0 1 16 0zM1 16h18" fill="#222" stroke="#222" stroke-width="1.5"/></svg>Meals includedImage</div>

<nav class="pager">
  <span class="disabled">« Previous</span><span class="current">1</span><span>2</span><span>3</span><span>Next »</span>
</nav>

<!-- footer -->
<svg class="footer-wave" viewBox="0 0 1200 90" preserveAspectRatio="none"><path d="M0 90C120 80 240 60 380 45S560 20 700 25 1000 60 1200 58V90z" fill="#000"/></svg>
<footer class="site-footer">
  <div class="fcol" style="left:274px"><h4>Legal information</h4><p>VELQORAMBE B.V. is registered with the trade register of the Chamber of Commerce in Utrecht, the Netherlands, under registration number 70012345.<br>VAT registration number is NL800012345B01.</p></div>
  <div class="fcol" style="left:385px"><h4>Velqorambe</h4><p>About Us<br>Contact Us<br>Terms and Conditions<br>Privacy</p></div>
  <div class="fcol" style="left:497px"><h4>Sustainability</h4><p>Our Climate Pledge<br>Our Progress<br>How It Works</p></div>
  <div class="fcol" style="left:608px"><h4>Our Partners</h4><p>Organizers<br>Arborline</p></div>
  <div class="fcol" style="left:719px;width:110px"><h4>Contact</h4><p>⌂ Amsterdam, the Netherlands<br>✉ info@velqorambe.com<br>☎ +01 200 400 10</p></div>
  <div class="copyright">© 2020 VELQORAMBE B.V.</div>
  <div class="connect">Connect With Us : <span class="social"></span><span class="social"></span><span class="social"></span><span class="social" style="background:#000"></span></div>
</footer>

</div>
</body>
</html>
```